UK Supplement Company Needs a Label for Diet Protein Powder

We need a new, modern and fresh design for our Diet Protein Powder. Our protein powder is packaged in black plastic tubs (photo attached) and needs an attractive label. We would like to see designs that grab attention and look professional. We're very open to ideas. The label should be 88mm x 365mm. We also prefer PSD format where possible. These alterations could be made once your design is chosen. Have attached photo of our shake ingredients/benefits.

Target Market(s)

Slimmers

Industry/Entity Type

Health And Wellness

Font styles to use
Serif
Sans Serif

Colors

Designer to choose colors to be used in the design.

Requirements
Must have
• Clean, Modern and Professional Look. Eye catching. The flavour, we offer 6 flavours so this must be something we can edit (Flavours are Banana, Chocolate, Chocolate Mint, Strawberry, Toffee and Vanilla).
Nice to have
• Our logo, this can be TALVEN Nutrition or just TALVEN. Our logo files are attached.
Should not have
• We do not want to see people (faces or bodies) on the design.

```html
<!DOCTYPE html>
<html lang="en">
<head>
<meta charset="utf-8">
<title>TALVEN Nutrition – Strawberry Protein Shake Label</title>
<link href="https://fonts.googleapis.com/css2?family=Montserrat:wght@300;400;500;600;700&display=swap" rel="stylesheet">
<style>
  :root {
    --page: #f1f1f1;
    --label: #141414;
    --white: #ffffff;
    --muted: #cfcfcf;
    --brand-red: #7c1d1f;
    --accent-red: #e8374b;
    --accent-pink: #f0566a;
    --rule-red: #8a2a2d;
    --badge: #1d3a2e;
    --badge-edge: #2c5140;
  }
  * { box-sizing: border-box; margin: 0; padding: 0; }
  html, body { width: 1008px; height: 1200px; overflow: hidden; }
  body {
    background: var(--page);
    font-family: "Montserrat", sans-serif;
    color: var(--white);
    position: relative;
  }
  .label {
    position: absolute;
    left: 24px; top: 484px;
    width: 960px; height: 232px;
    background: var(--label);
    overflow: hidden;
  }
  .abs { position: absolute; }
  .centered { left: 0; width: 960px; text-align: center; }

  /* left panel */
  .nutrition {
    left: 27px; top: 19px; width: 269px; height: 76px;
    background: var(--white); color: #000;
    border: 2px solid #000; outline: 1px solid var(--white);
    display: flex; gap: 3px; padding: 3px 4px; font-size: 4.6px; line-height: 1.35;
  }
  .nutrition .head { width: 76px; flex: none; }
  .nutrition .title { font-size: 12px; font-weight: 700; line-height: 1.05; }
  .nutrition table { border-collapse: collapse; flex: 1; }
  .nutrition th { font-weight: 600; text-align: left; border-bottom: 1.5px solid #000; }
  .nutrition td { border-bottom: 0.5px solid #000; padding: 0 2px; }
  .nutrition td.r { text-align: right; font-weight: 700; }
  .caution-title { left: 24px; top: 127px; font-size: 9px; font-weight: 500; letter-spacing: .3px; }
  .caution-text { left: 24px; top: 143px; width: 248px; font-size: 6px; line-height: 1.55; color: var(--muted); }
  .maker { left: 12px; top: 216px; font-size: 5.5px; color: var(--muted); }

  /* front panel */
  .logo-box {
    left: 414px; top: 0; width: 132px; height: 62px;
    background: var(--brand-red); border-radius: 0 0 4px 4px;
    display: flex; align-items: center; justify-content: center;
  }
  .logo-name { font-size: 24px; font-weight: 700; letter-spacing: -.3px; color: var(--white); }
  .category { top: 68px; font-size: 14px; font-weight: 300; letter-spacing: .3px; }
  .rule { left: 358px; top: 92px; width: 244px; height: 1px; background: var(--rule-red); }
  .product-line1 { top: 98px; font-size: 15.5px; font-weight: 400; letter-spacing: .4px; }
  .product-line2 { top: 123px; font-size: 15.5px; font-weight: 400; letter-spacing: .4px; }
  .product-line2 .highlight { background: var(--brand-red); font-weight: 600; padding: 0 3px; border-radius: 2px; }
  .stat { font-size: 8.5px; font-weight: 400; text-align: center; }
  .stat small { display: block; font-size: 4.5px; color: var(--muted); letter-spacing: .3px; }
  .stat-cal { left: 358px; top: 151px; }
  .stat-carb { left: 547px; top: 151px; }
  .fruit { left: 462px; top: 152px; width: 36px; height: 27px; border-radius: 50%;
    background: radial-gradient(circle at 45% 60%, #d8222c 0%, #b3161f 65%, #2f7a22 100%); }
  .flavour { top: 180px; font-size: 8px; font-weight: 700; color: var(--accent-red); line-height: 1; }
  .flavour small { display: block; font-size: 4px; color: var(--muted); font-weight: 400; margin-top: 1px; }
  .badges { left: 350px; top: 198px; display: flex; gap: 3px; }
  .badge {
    width: 22px; height: 22px; background: var(--badge); border: 1px solid var(--badge-edge);
    font-size: 4.8px; font-weight: 700; text-align: center; padding-top: 4px; line-height: 1.1;
  }
  .badge.big { font-size: 8px; padding-top: 2px; }
  .badge small { display: block; font-size: 2.8px; font-weight: 400; }
  .wave { left: 318px; top: 185px; width: 322px; height: 47px; }

  /* right panel */
  .info { right: 17px; width: 252px; text-align: right; }
  .info h3 { font-size: 8px; font-weight: 500; letter-spacing: .3px; margin-bottom: 14px; }
  .info p { font-size: 5.5px; line-height: 1.65; color: var(--muted); }
  .info-rule { right: 17px; width: 265px; height: 1px; background: var(--muted); }
  .use { top: 38px; }
  .ingredients { top: 100px; }
  .allergens { top: 163px; }
</style>
</head>
<body>
<main class="label">
  <!-- back-left panel -->
  <section class="abs nutrition">
    <div class="head">
      <div class="title">Nutrition<br>Facts</div>
      Serving Size 2 scoops (38g)<br>Servings Per Container 6<br><b>Calories</b> 220<br>&nbsp;Calories from Fat 160<br>*Daily Values on 2,000 kcal diet.
    </div>
    <table>
      <tr><th>Amount / Serving</th><th>% DV*</th><th>Amount / Serving</th><th>% DV*</th></tr>
      <tr><td><b>Total Fat</b> 18g</td><td class="r">28%</td><td><b>Total Carbohydrate</b> 16g</td><td class="r">5%</td></tr>
      <tr><td>&nbsp;Saturated Fat 4g</td><td class="r">20%</td><td>&nbsp;Dietary Fiber 2g</td><td class="r">8%</td></tr>
      <tr><td>&nbsp;Trans Fat 0g</td><td></td><td>&nbsp;Sugars 11g</td><td></td></tr>
      <tr><td><b>Cholesterol</b> 5mg</td><td class="r">2%</td><td><b>Protein</b> 2g</td><td></td></tr>
      <tr><td><b>Sodium</b> 20mg</td><td class="r">1%</td><td></td><td></td></tr>
      <tr><td>Vitamin A 2% &bull; Vitamin C 0%</td><td></td><td>Calcium 4% &bull; Iron 4%</td><td></td></tr>
    </table>
  </section>
  <h3 class="abs caution-title">CAUTION:</h3>
  <p class="abs caution-text">This product should not be used as a substitute for a balanced and healthy lifestyle. Not recomended for use by pregnant or loctating women. If you are taking any medications or under medical supervission, you should consult with your GP before use. Not intended for use by persons under the age of 18. Not intended for long term usage.</p>
  <p class="abs maker">Manufactured in the uk for talven nutrition limited, mill lane, eastford, ex1 2ab.</p>

  <!-- front panel -->
  <svg class="abs wave" viewBox="0 0 322 47" preserveAspectRatio="none" aria-hidden="true">
    <path d="M0 47 C90 40 180 12 270 10 C300 10 315 28 322 47 Z" fill="var(--accent-red)"/>
    <path d="M110 47 C180 32 240 18 285 20 C305 22 316 34 322 47 Z" fill="var(--accent-pink)" opacity=".85"/>
  </svg>
  <div class="abs logo-box"><span class="logo-name">TALVEN</span></div>
  <p class="abs centered category">DIETARY SUPPLEMENT</p>
  <div class="abs rule"></div>
  <h1 class="abs centered product-line1">LAW CALORIE</h1>
  <h2 class="abs centered product-line2"><span class="highlight">PROTIEN</span> SHAKE</h2>
  <p class="abs stat stat-cal">117 CALORIES<small>PER SERVING</small></p>
  <p class="abs stat stat-carb">4.2 CARBS<small>PER SERVING</small></p>
  <div class="abs fruit" role="img" aria-label="Strawberries illustration"></div>
  <p class="abs centered flavour">STRAWBERRY<small>FLAVOUR</small></p>
  <div class="abs badges">
    <div class="badge">120 MG<small>GREEN TEA EXTRACT</small></div>
    <div class="badge big">21G<small>PROTIEN</small></div>
    <div class="badge">120 MG<small>ACAI BERRY</small></div>
    <div class="badge">15 MG<small>CLR POWDER</small></div>
  </div>

  <!-- back-right panel -->
  <section class="abs info use">
    <h3>SUGGESTED USE:</h3>
    <p>Mix one level scoop (30g) with at least 200ml of cold water or skimmed milk in a shaker. reseal pouch after each use. store in cool and dry place. Keep away from children.</p>
  </section>
  <div class="abs info-rule" style="top:92px"></div>
  <section class="abs info ingredients">
    <h3>INGREDIENTS:</h3>
    <p>protein Blend (soys protein Isolate, Whey protein concintrate (MILK), MILK PROTEIN), Acety-L-Carmitine, Acai Berry Extract, Green Tea Extract, CLA Powder, Flavourings, Colorings, Xanthan Gum, Sweetener: Sucralose.</p>
  </section>
  <div class="abs info-rule" style="top:155px"></div>
  <section class="abs info allergens">
    <h3>ALLERGENS:</h3>
    <p>for alergers, see ingredients in bold, Processed on equipment which also processes gluten, nuts egg and peanuts</p>
  </section>
</main>
</body>
</html>
```